Brelton Services - Fast, Efficient and Gas Mainteance for Domestic, Commercial and Industrial clients

We are in the process of purchasing a new business and would like to get a new logo and business card.
Business is a gas maintenance business that also does new gas installations.
Has been established since 1988.
Services include:
Install all types of gas appliances & equipment inc. hot water units
Maintain / repair / replace all types of gas appliances & equipment

Target Market(s)

Domestic, Commercial and Industrial clients

Industry/Entity Type

Business

Contact Information for Business Card

admin@breltonservices.example.au
07 5382 4690
Brelton Services PTY LTD

Logo Text

Gas Fitting & Plumbing Maintenance Specialists

Font styles to use
Sans Serif

Requirements
Must have
• Logo
• Business name, contact number, email address, web address
• Domestic | Commercial | Industrial Est Since 1988
Nice to have
• Possibly a black card with a flame logo to one side
Should not have
• Spelling errors

```html
<!DOCTYPE html>
<html lang="en">
<head>
<meta charset="utf-8">
<title>Brelton Services – Business Card</title>
<link href="https://fonts.googleapis.com/css2?family=Open+Sans:wght@400;600;700&family=Great+Vibes&display=swap" rel="stylesheet">
<style>
  :root {
    --bg: #e4e1dc;
    --card: #f4f4f3;
    --accent: #ec5a33;
    --ink: #3a3d45;
    --muted: #6d7078;
    --script: #8a8c90;
  }
  * { box-sizing: border-box; margin: 0; padding: 0; }
  html, body { width: 1200px; height: 892px; overflow: hidden; }
  body {
    background: var(--bg);
    font-family: "Open Sans", Arial, sans-serif;
    display: flex;
    flex-direction: column;
    align-items: center;
    justify-content: center;
    gap: 40px;
  }
  .card {
    width: 640px;
    height: 392px;
    background: var(--card);
    box-shadow: 0 6px 18px rgba(0,0,0,.18);
    position: relative;
    overflow: hidden;
  }
  .card--front { height: 392px; }

  /* front */
  .front-brand { position: absolute; left: 70px; top: 120px; }
  .brand-name {
    display: flex; align-items: center; gap: 14px;
    color: var(--accent);
    font-weight: 700;
    font-size: 42px;
    letter-spacing: 1px;
    text-transform: uppercase;
    line-height: 1;
  }
  .brand-dot { width: 18px; height: 18px; border-radius: 50%; background: var(--accent); flex: none; }
  .tagline { color: var(--ink); font-weight: 700; font-size: 26px; margin-top: 12px; }
  .sectors-row { display: flex; align-items: baseline; gap: 18px; margin-top: 10px; }
  .sectors { color: var(--muted); font-size: 15px; letter-spacing: .5px; }
  .established { font-family: "Great Vibes", cursive; color: var(--script); font-size: 26px; }

  /* back */
  .back-header { position: absolute; right: 40px; top: 34px; text-align: right; }
  .back-header .brand-name { font-size: 32px; justify-content: flex-end; }
  .pty { font-size: 10px; font-weight: 700; color: var(--ink); margin-left: 4px; align-self: flex-end; }
  .back-header .tagline { font-size: 21px; margin-top: 8px; }
  .back-header .sectors-row { justify-content: flex-end; margin-top: 4px; }
  .back-header .sectors { font-size: 12px; }
  .back-header .established { font-size: 22px; }
  .divider { position: absolute; left: 0; right: 0; top: 172px; height: 2px; background: var(--accent); }
  .contacts { position: absolute; left: 40px; top: 196px; list-style: none; }
  .contact { display: flex; align-items: center; gap: 14px; font-size: 19px; color: #222; line-height: 1; margin-bottom: 12px; }
  .contact-icon { width: 18px; height: 18px; background: var(--accent); border-radius: 2px; display: flex; align-items: center; justify-content: center; flex: none; }
  .contact-icon svg { width: 12px; height: 12px; fill: #fff; }
</style>
</head>
<body>

<section class="card card--front" aria-label="Business card front">
  <div class="front-brand">
    <div class="brand-name"><span class="brand-dot"></span>Brelton Services</div>
    <p class="tagline">Gas fitting &amp; Plumbing Specialists</p>
    <div class="sectors-row">
      <span class="sectors">Domestic | Commercial | Industrial</span>
      <span class="established">Est Since 1988</span>
    </div>
  </div>
</section>

<section class="card card--back" aria-label="Business card back">
  <header class="back-header">
    <div class="brand-name">Brelton Services<span class="pty">PTY LTD</span></div>
    <p class="tagline">Gas fitting &amp; Plumbing Specialists</p>
    <div class="sectors-row">
      <span class="sectors">Domestic | Commercial | Industrial</span>
      <span class="established">Est Since 1988</span>
    </div>
  </header>
  <div class="divider"></div>
  <ul class="contacts">
    <li class="contact"><span class="contact-icon"><svg viewBox="0 0 12 12"><path d="M2.5 1h2l1 2.5-1.3 1a6 6 0 0 0 3.3 3.3l1-1.3L11 7.5v2c0 .8-.7 1.5-1.5 1.5A8.5 8.5 0 0 1 1 2.5C1 1.7 1.7 1 2.5 1z"/></svg></span>07 5382 4690</li>
    <li class="contact"><span class="contact-icon"><svg viewBox="0 0 12 12"><rect x="3" y="1" width="6" height="3"/><rect x="1" y="4.5" width="10" height="5" rx="1"/><rect x="3" y="8" width="6" height="3"/></svg></span>07 5382 4712</li>
    <li class="contact"><span class="contact-icon"><svg viewBox="0 0 12 12"><circle cx="6" cy="6" r="5" fill="none" stroke="#fff" stroke-width="1.3"/><path d="M1 6h10M6 1c2 2 2 8 0 10M6 1c-2 2-2 8 0 10" fill="none" stroke="#fff" stroke-width="1"/></svg></span>www.breltonservices.example.au</li>
    <li class="contact"><span class="contact-icon"><svg viewBox="0 0 12 12"><rect x="1" y="2.5" width="10" height="7" fill="none" stroke="#fff" stroke-width="1.3"/><path d="M1 3l5 4 5-4" fill="none" stroke="#fff" stroke-width="1.2"/></svg></span>admin@breltonservices.example.au</li>
    <li class="contact"><span class="contact-icon"><svg viewBox="0 0 12 12"><path d="M6 1a3.5 3.5 0 0 0-3.5 3.5C2.5 7.5 6 11 6 11s3.5-3.5 3.5-6.5A3.5 3.5 0 0 0 6 1zm0 5a1.5 1.5 0 1 1 0-3 1.5 1.5 0 0 1 0 3z"/></svg></span>PO Box 2846, Carrow Heads, QLD 4299</li>
  </ul>
</section>

</body>
</html>
```